Emergency Management Consulting Flyer

Company name: Stone Harbor Emergency Management

I am looking for a postcard design for my emergency management consulting business. I'm looking for something that has some colors and is double sided, on side with the information on services provided and the other side with the contact information. For the main side I'm looking for the following:

How prepared are you?

Services Provided:
Healthcare Preparedness
EOC Support
Emergency Planning
Mitigation Planning
Business Continuity
Disaster Response
Training and Exercises
Project Management
And more

Affordable for small and large organizations
Stand-by contracts available

On the back side, I'm looking for Contact Us section.

Overall I'm looking for something a bit more modern and need to have at least one disaster photo. If you have questions please message me.

Target Market(s)

Government, Healthcare Facilities, Businesses

Industry/Entity Type

Consulting

Requirements
Must have
• Disaster Picture, modern looking
• For the main side I'm looking for the following:
• How prepared are you?
• Services Provided:
• Healthcare Preparedness
• EOC Support
• Emergency Planning
• Mitigation Planning
• Business Continuity
• Disaster Response
• Training and Exercises
• Project Management
• And more
• Affordable for small and large organizations
• Stand-by contracts available

```html
<!DOCTYPE html>
<html lang="en">
<head>
<meta charset="utf-8">
<title>Stone Harbor Emergency Management – Postcard</title>
<link rel="stylesheet" href="https://fonts.googleapis.com/css2?family=Montserrat:wght@500;600;700;800;900&family=Arimo:wght@700&display=swap">
<style>
  :root {
    --orange: #e5661a;
    --orange-light: #ef7d22;
    --navy: #22235f;
    --navy-text: #26267a;
    --black: #1b1b1b;
    --white: #ffffff;
    --paper: #ffffff;
    --ink: #1d1d1d;
    --rule: #b9b9b9;
    --stage: #ece9e4;
    --badge-bg: #e9eaec;
    --brand-text: #3f4650;
  }
  * { box-sizing: border-box; margin: 0; padding: 0; }
  html, body { width: 1200px; height: 1000px; overflow: hidden; }
  body {
    position: relative;
    background: var(--stage);
    font-family: "Montserrat", Arial, sans-serif;
  }

  /* ---------- front side ---------- */
  .card-front {
    position: absolute;
    left: 40px; top: 30px;
    width: 605px; height: 467px;
    overflow: hidden;
    box-shadow: 0 6px 18px rgba(0,0,0,.25);
    background: var(--orange);
  }
  .card-front .shapes { position: absolute; inset: 0; }
  .photo-area {
    position: absolute; left: 295px; top: 0;
    width: 310px; height: 385px;
    clip-path: polygon(55px 0, 310px 0, 310px 385px, 0 385px);
  }
  .brand-badge {
    position: absolute;
    left: 43px; top: 42px;
    width: 284px; height: 63px;
    background: var(--badge-bg);
    display: flex; align-items: center; gap: 12px;
    padding-left: 16px;
  }
  .brand-dot {
    width: 38px; height: 38px; border-radius: 50%;
    background: var(--orange);
    flex: none;
  }
  .brand-name {
    font-weight: 800;
    color: var(--brand-text);
    font-size: 13.5px;
    line-height: 1.25;
    letter-spacing: .4px;
    text-transform: uppercase;
    white-space: nowrap;
  }
  .headline { position: absolute; left: 33px; top: 124px; width: 260px; }
  .headline span { display: block; font-weight: 900; line-height: 1; }
  .headline .how { color: var(--white); font-size: 27px; }
  .headline .prepared {
    color: var(--navy-text); font-size: 40px; letter-spacing: -.5px;
    text-shadow:
      1.5px 0 0 var(--white), -1.5px 0 0 var(--white),
      0 1.5px 0 var(--white), 0 -1.5px 0 var(--white),
      1px 1px 0 var(--white), -1px -1px 0 var(--white),
      1px -1px 0 var(--white), -1px 1px 0 var(--white);
    margin-top: 1px;
  }
  .headline .are { color: var(--white); font-size: 23px; text-align: right; padding-right: 10px; margin-top: 1px; }
  .headline-rule {
    position: absolute; left: 37px; top: 218px;
    width: 240px; height: 3px;
    background: linear-gradient(90deg, transparent, #8a3a0d 20%, #8a3a0d 80%, transparent);
  }
  .services-tag {
    position: absolute; left: 43px; top: 235px;
    padding: 3px 6px 4px;
    border: 1.5px dashed var(--white);
    border-radius: 4px;
    background: var(--orange-light);
    font-weight: 800; font-size: 19px; color: var(--ink);
  }
  .services-list {
    position: absolute; left: 32px; top: 272px;
    list-style: none;
    color: var(--white);
    font-weight: 600; font-size: 14.5px; line-height: 18.6px;
  }
  .services-list li { display: flex; align-items: center; gap: 5px; }
  .services-list li svg { width: 13px; height: 13px; flex: none; }
  .services-list li.more { padding-left: 18px; }
  .front-contact {
    position: absolute; left: 318px; top: 385px;
    width: 287px; height: 82px;
    display: flex; align-items: center; justify-content: center;
    color: var(--white);
    font-family: "Arimo", Arial, sans-serif; font-weight: 700; font-size: 21px;
    padding-left: 14px;
  }

  /* ---------- back side ---------- */
  .card-back {
    position: absolute;
    left: 557px; top: 506px;
    width: 606px; height: 469px;
    background: var(--paper);
    box-shadow: 0 6px 18px rgba(0,0,0,.25);
  }
  .offer-panel {
    position: absolute; left: 0; top: 0;
    width: 295px; height: 208px;
    background: var(--orange);
    border-bottom-right-radius: 16px;
    color: var(--white);
    font-family: "Arimo", Arial, sans-serif; font-weight: 700;
    font-size: 16.5px; line-height: 20px;
    text-align: center;
  }
  .offer-panel p { position: absolute; left: 0; width: 100%; }
  .offer-panel .offer-size { top: 37px; }
  .offer-panel .offer-standby { top: 139px; }
  .offer-rule {
    position: absolute; left: 40px; top: 114px;
    width: 215px; height: 3px;
    background: linear-gradient(90deg, transparent, #8a3a0d 20%, #8a3a0d 80%, transparent);
  }
  .contact-panel {
    position: absolute; left: 0; top: 190px;
    width: 295px; height: 184px;
    border: 1px solid #c9c9c9; border-top: none; border-left: none;
    border-bottom-right-radius: 16px;
  }
  .contact-tab {
    position: absolute; left: 76px; top: 210px;
    width: 144px; height: 24px;
    background: var(--black);
    clip-path: polygon(0 0, 100% 0, 94% 100%, 6% 100%);
    color: var(--white);
    font-family: "Arimo", Arial, sans-serif; font-weight: 700; font-size: 13.5px;
    display: flex; align-items: center; justify-content: center;
  }
  .back-brand {
    position: absolute; left: 20px; top: 240px;
    width: 262px; height: 50px;
    display: flex; align-items: center; gap: 10px;
  }
  .back-brand .brand-dot { width: 36px; height: 36px; }
  .back-brand .brand-name { font-size: 13.5px; }
  .back-contact {
    position: absolute; left: 0; top: 316px; width: 305px;
    text-align: center;
    font-family: "Arimo", Arial, sans-serif; font-weight: 700; font-size: 20px;
    color: var(--ink);
  }
  .stamp-box {
    position: absolute; left: 483px; top: 34px;
    width: 91px; height: 92px;
    border: 1px solid #9a9a9a;
  }
  .address-line {
    position: absolute; left: 345px;
    width: 225px; height: 1px;
    background: var(--rule);
  }
  .address-line.first { top: 221px; }
  .address-line.second { top: 297px; }
</style>
</head>
<body>

<section class="card-front" aria-label="Postcard front">
  <svg class="shapes" width="605" height="467" viewBox="0 0 605 467" aria-hidden="true">
    <defs>
      <linearGradient id="orangeTone" x1="0" y1="0" x2="1" y2="1">
        <stop offset="0" stop-color="#ec7120"/>
        <stop offset="1" stop-color="#e05f16"/>
      </linearGradient>
      <linearGradient id="photoTone" x1="0" y1="0" x2="0" y2="1">
        <stop offset="0" stop-color="#9fb3c8"/>
        <stop offset=".45" stop-color="#a7a9ab"/>
        <stop offset="1" stop-color="#5b5a55"/>
      </linearGradient>
    </defs>
    <polygon points="280,180 380,180 380,467 238,467" fill="var(--navy)"/>
    <polygon points="350,0 605,0 605,385 295,385" fill="url(#photoTone)"/>
    <polygon points="318,385 605,385 605,467 300,467" fill="var(--black)"/>
    <polygon points="0,0 350,0 238,467 0,467" fill="url(#orangeTone)"/>
  </svg>
  <div class="photo-area" role="img" aria-label="Photo: rescue workers standing in the rubble of collapsed apartment towers after an earthquake"></div>

  <div class="brand-badge">
    <span class="brand-dot" aria-hidden="true"></span>
    <span class="brand-name">Stone Harbor<br>Emergency Management</span>
  </div>

  <h1 class="headline">
    <span class="how">HOW</span>
    <span class="prepared">PREPARED</span>
    <span class="are">ARE YOU ?</span>
  </h1>
  <div class="headline-rule" aria-hidden="true"></div>

  <h2 class="services-tag">Services Provided</h2>
  <ul class="services-list">
    <li><svg viewBox="0 0 14 14"><path d="M1 7.5 L5 11.5 L13 2" fill="none" stroke="#fff" stroke-width="1.8"/></svg>Healthcare Preparedness</li>
    <li><svg viewBox="0 0 14 14"><path d="M1 7.5 L5 11.5 L13 2" fill="none" stroke="#fff" stroke-width="1.8"/></svg>EOC Support</li>
    <li><svg viewBox="0 0 14 14"><path d="M1 7.5 L5 11.5 L13 2" fill="none" stroke="#fff" stroke-width="1.8"/></svg>Emergency Planning</li>
    <li><svg viewBox="0 0 14 14"><path d="M1 7.5 L5 11.5 L13 2" fill="none" stroke="#fff" stroke-width="1.8"/></svg>Mitigation Planning</li>
    <li><svg viewBox="0 0 14 14"><path d="M1 7.5 L5 11.5 L13 2" fill="none" stroke="#fff" stroke-width="1.8"/></svg>Business Continuity</li>
    <li><svg viewBox="0 0 14 14"><path d="M1 7.5 L5 11.5 L13 2" fill="none" stroke="#fff" stroke-width="1.8"/></svg>Disaster Response</li>
    <li><svg viewBox="0 0 14 14"><path d="M1 7.5 L5 11.5 L13 2" fill="none" stroke="#fff" stroke-width="1.8"/></svg>Training and Exercises</li>
    <li><svg viewBox="0 0 14 14"><path d="M1 7.5 L5 11.5 L13 2" fill="none" stroke="#fff" stroke-width="1.8"/></svg>Project Management</li>
    <li class="more">And more</li>
  </ul>

  <div class="front-contact">CONTACT DETAILS</div>
</section>

<section class="card-back" aria-label="Postcard back">
  <div class="contact-panel" aria-hidden="true"></div>
  <div class="offer-panel">
    <p class="offer-size">AFFORDABLE FOR<br>SMALL AND<br>LARGE ORGANIZATIONS</p>
    <div class="offer-rule" aria-hidden="true"></div>
    <p class="offer-standby">STAND-BY CONTRACTS<br>AVAILABLE</p>
  </div>
  <div class="contact-tab">CONTACT US AT</div>
  <div class="back-brand">
    <span class="brand-dot" aria-hidden="true"></span>
    <span class="brand-name">Stone Harbor<br>Emergency Management</span>
  </div>
  <div class="back-contact">CONTACT DETAILS</div>

  <div class="stamp-box" aria-hidden="true"></div>
  <div class="address-line first" aria-hidden="true"></div>
  <div class="address-line second" aria-hidden="true"></div>
</section>

</body>
</html>
```